Project Planning & Communication Process

Need a PowerPoint slide that illustrates our project planning and communication cycle. Our company has key meetings, and key communication vehicles (like emails and follow up tools) that we use to ensure our frontline staff are prepared to execute the new project successfully. This document needs to call out how the different components, like the meetings and emails, work together (like a flow chart), so someone who needs to use this process will understand what they should do. The slide needs to be simple yet comprehensive enough to guide someone through the details. I don't want it overwhelming. The primary focus is the process, not the details.

Use the color pallette included within the slide (shades of blue and gray, and black). This is for an insurance company (www.marrowpine.com). Use this as a reference for the look and feel.

I have attached a sample slide of the flow chart process.

Click here if you cannot access the file. https://www.stashloft.com/s/qx7rmt2pbn9wkaz/Communcation_Methods_V1.pptx

If you are not able to see the uploaded slide.  Please send me your email address and I will send the slide to you directly. 

ISince I'm not able to upload the reference ppt file, 've uploaded the slide at StashLoft.  Please click here to access.
https://www.stashloft.com/s/qx7rmt2pbn9wkaz/Communcation_Methods_V1.pptx

Reason: extending one more day for designers to make last minute updates.

Target Market(s)

Vice Presidents and project managers/business partners within the organization.

Industry/Entity Type

Communication

Font styles to use
Sans Serif

Colors
3176b5

Requirements
Must have
• 1 page, color pallette assigned, be simple yet comprehensive. the focus needs to be on the process, not on the details.
Nice to have
• Doesn't have to follow the example I provided. Please feel free to approach from different ways.

```html
<!DOCTYPE html>
<html lang="en">
<head>
<meta charset="utf-8">
<title>Project Alignment &amp; Project Communication Process</title>
<link rel="stylesheet" href="https://fonts.googleapis.com/css2?family=Titillium+Web:ital,wght@0,400;0,600;0,700;1,400&display=swap">
<style>
  :root {
    --slate: #3b4353;
    --arrow-dark: #3a4250;
    --timeline-blue: #3f6fb8;
    --marker-red: #e0554a;
    --step-light: #8ab8e1;
    --step-light-tab: #9cc4e8;
    --step-mid: #4a7fbe;
    --step-mid-tab: #5088c6;
    --step-dark: #1c3454;
    --step-dark-tab: #1c3454;
    --panel-gray: #e1e1e1;
    --panel-blue: #3e75b5;
    --panel-red: #e5695a;
    --ribbon-gray: #c8c8c8;
    --text-dark: #333a44;
    --label-blue: #3176b5;
    --icon-gray: #c5cbd4;
    --white: #ffffff;
  }
  * { box-sizing: border-box; margin: 0; padding: 0; }
  html, body { width: 1200px; height: 900px; overflow: hidden; background: var(--white); }
  body { font-family: "Titillium Web", Arial, sans-serif; color: var(--text-dark); }
  .slide { position: relative; width: 1200px; height: 900px; overflow: hidden; }

  .header {
    position: absolute; left: 0; top: 0; width: 1200px; height: 82px;
    background: var(--slate); display: flex; align-items: center; justify-content: center;
  }
  .header h1 {
    font-family: "Titillium Web", Arial, sans-serif; font-weight: 700;
    font-size: 35px; color: var(--white); letter-spacing: 0.2px;
  }

  .timeline {
    position: absolute; left: 0; top: 172px; width: 1200px; height: 0;
    border-top: 3px dotted var(--timeline-blue);
  }
  .milestone {
    position: absolute; top: 147px; height: 45px; background: var(--white);
    border: 3px dotted var(--marker-red);
    display: flex; align-items: center; justify-content: center;
    font-size: 10px; color: var(--text-dark);
  }

  .step-icon {
    position: absolute; top: 214px; width: 56px; height: 54px; border-radius: 6px;
  }
  .step-icon.light { background: var(--step-light); }
  .step-icon.mid { background: var(--step-mid); }
  .step-icon.dark { background: var(--step-dark); }

  .step { position: absolute; top: 289px; width: 83px; }
  .step-number {
    height: 22px; display: flex; align-items: center; justify-content: center;
    font-style: italic; font-size: 23px; color: var(--white); line-height: 1;
  }
  .step-body {
    margin-top: 4px; height: 228px; padding-top: 22px; text-align: center;
    clip-path: polygon(0 0, 100% 0, 100% 100%, 50% 85%, 0 100%);
    color: var(--white); font-size: 15px; line-height: 18px; position: relative;
    white-space: nowrap;
  }
  .step.light .step-number { background: var(--step-light-tab); }
  .step.light .step-body { background: var(--step-light); }
  .step.mid .step-number { background: var(--step-mid-tab); }
  .step.mid .step-body { background: var(--step-mid); }
  .step.dark .step-number { background: var(--step-dark-tab); }
  .step.dark .step-body { background: var(--step-dark); }
  .step-note {
    position: absolute; left: 6px; right: 0; top: 164px; text-align: left;
    font-size: 8px; line-height: 10px; color: var(--white);
  }
  .asterisk { color: var(--marker-red); }
  .sup-asterisk { color: var(--marker-red); position: relative; top: -6px; font-size: 12px; }

  .flow-arrow {
    position: absolute; top: 353px; width: 22px; height: 22px; background: var(--arrow-dark);
    clip-path: polygon(0 25%, 45% 25%, 45% 0, 100% 50%, 45% 100%, 45% 75%, 0 75%);
  }

  .divider {
    position: absolute; left: 0; top: 691px; width: 1200px; height: 0;
    border-top: 3px dotted var(--slate);
  }

  .purposes {
    position: absolute; left: 0; top: 697px; width: 670px; height: 203px;
    background: var(--panel-gray); padding: 2px 0 0 4px;
    font-size: 11px; line-height: 14px; color: var(--text-dark);
    white-space: nowrap; overflow: hidden;
  }
  .purpose { margin-bottom: 14px; }
  .purpose .label { color: var(--label-blue); font-weight: 600; }
  .purpose .overview { padding-left: 20px; }

  .phases {
    position: absolute; left: 670px; top: 692px; width: 374px; height: 208px;
    background: var(--panel-blue);
  }
  .phase { position: absolute; left: 30px; width: 325px; height: 60px; }
  .phase-tag {
    position: absolute; left: 52px; top: 6px; width: 272px; height: 48px;
    background: var(--white);
    clip-path: polygon(0 0, 91% 0, 100% 50%, 91% 100%, 0 100%);
    display: flex; align-items: center; padding-left: 30px;
    font-style: italic; font-size: 16px; color: var(--text-dark); white-space: nowrap;
  }
  .phase-icon {
    position: absolute; left: 0; top: 0; width: 60px; height: 60px; border-radius: 50%;
    background: var(--white); border: 3px solid var(--panel-blue);
    box-shadow: 0 0 0 2px var(--white); z-index: 1;
  }
  .phase-icon span {
    position: absolute; inset: 12px; border-radius: 4px; background: var(--icon-gray);
  }

  .channels {
    position: absolute; left: 1044px; top: 692px; width: 156px; height: 208px;
    background: var(--panel-red); text-align: center; color: var(--white);
  }
  .ribbon {
    position: absolute; left: 20px; width: 116px; height: 28px;
    display: flex; align-items: center; justify-content: center; font-size: 15px;
    clip-path: polygon(0 0, 100% 0, 93% 50%, 100% 100%, 0 100%, 7% 50%);
  }
  .ribbon.meetings { top: 44px; background: var(--ribbon-gray); color: var(--white); }
  .ribbon.tools { top: 112px; background: var(--slate); color: var(--white); }
  .channel-steps { position: absolute; left: 0; width: 156px; font-size: 15px; white-space: nowrap; }
</style>
</head>
<body>
<div class="slide">
  <header class="header"><h1>Project Alignment &amp; Project Communication Process</h1></header>

  <div class="timeline"></div>
  <div class="milestone" style="left:136px;width:91px;">3+ Months Out</div>
  <div class="milestone" style="left:495px;width:93px;">2+ Months Out</div>
  <div class="milestone" style="left:729px;width:93px;">1 Month Out</div>
  <div class="milestone" style="left:850px;width:94px;">1 Week Out</div>

  <div class="step-icon light" style="left:36px;" role="img" aria-label="Light bulb icon"></div>
  <div class="step-icon light" style="left:155px;" role="img" aria-label="Icon of people around a meeting table"></div>
  <div class="step-icon light" style="left:274px;" role="img" aria-label="Icon of two people in conversation"></div>
  <div class="step-icon light" style="left:393px;" role="img" aria-label="Icon of people around a meeting table"></div>
  <div class="step-icon light" style="left:512px;" role="img" aria-label="Icon of a leader linked to a team"></div>
  <div class="step-icon mid" style="left:632px;" role="img" aria-label="Icon of two people shaking hands"></div>
  <div class="step-icon mid" style="left:751px;" role="img" aria-label="Icon of a leader linked to a team"></div>
  <div class="step-icon mid" style="left:871px;" role="img" aria-label="Icon of a group receiving a memo"></div>
  <div class="step-icon mid" style="left:990px;" role="img" aria-label="Icon of a presenter at a board"></div>
  <div class="step-icon dark" style="left:1109px;" role="img" aria-label="Icon of a person at a desk with a team"></div>

  <div class="step light" style="left:22px;"><div class="step-number">1</div><div class="step-body">New<br>Project<br>Identified</div></div>
  <div class="step light" style="left:141px;"><div class="step-number">2</div><div class="step-body">Governance<br>Meeting</div></div>
  <div class="step light" style="left:260px;"><div class="step-number">3</div><div class="step-body">Separate<br>Project<br>Meetings<br>as needed</div></div>
  <div class="step light" style="left:379px;"><div class="step-number">4</div><div class="step-body">Governance<br>Meeting</div></div>
  <div class="step light" style="left:498px;"><div class="step-number">5</div><div class="step-body">Weekly<span class="sup-asterisk">*</span><br>Center<br>leader<br>Meeting<div class="step-note"><span class="asterisk">*</span> to collect feedback</div></div></div>
  <div class="step mid" style="left:618px;"><div class="step-number">6</div><div class="step-body">Field<br>Advisory<br>Panel</div></div>
  <div class="step mid" style="left:737px;"><div class="step-number">7</div><div class="step-body">Weekly<span class="sup-asterisk">*</span><br>Center<br>Leader<br>Meeting<div class="step-note"><span class="asterisk">*</span> Center Planning<br>&nbsp;&nbsp;and Specific<br>&nbsp;&nbsp;execution details</div></div></div>
  <div class="step mid" style="left:857px;"><div class="step-number">8</div><div class="step-body">Monday<br>Memo</div></div>
  <div class="step mid" style="left:976px;"><div class="step-number">9</div><div class="step-body">Daily<br>Digest</div></div>
  <div class="step dark" style="left:1095px;"><div class="step-number">10</div><div class="step-body">Follow<br>Up<br>Guide</div></div>

  <div class="flow-arrow" style="left:112px;"></div>
  <div class="flow-arrow" style="left:231px;"></div>
  <div class="flow-arrow" style="left:350px;"></div>
  <div class="flow-arrow" style="left:469px;"></div>
  <div class="flow-arrow" style="left:589px;"></div>
  <div class="flow-arrow" style="left:708px;"></div>
  <div class="flow-arrow" style="left:828px;"></div>
  <div class="flow-arrow" style="left:947px;"></div>
  <div class="flow-arrow" style="left:1066px;"></div>

  <div class="divider"></div>

  <section class="purposes">
    <div class="purpose">2 - &nbsp;<span class="label">Purpose:</span> Go/No Go Decision<div class="overview"><span class="label">Overview:</span> Project Owner presents one pager to Sr Leadership. Based on Business Value, and Capacity a Go/No Go Decision is made.</div></div>
    <div class="purpose">4 - &nbsp;<span class="label">Purpose:</span> Report out on Milestone status and Key Decision Points<div class="overview"><span class="label">Overview:</span> Project Owner presents milestones and feedback/approvals during key decision points.</div></div>
    <div class="purpose">5 - &nbsp;<span class="label">Purpose:</span> Introduce Project &amp; gather Center Leader Feedback<div class="overview"><span class="label">Overview:</span> Project Owner provides overview of project, collects center leader feedback.</div></div>
    <div class="purpose">6 - &nbsp;<span class="label">Purpose:</span> Collect Center Staff Feedback<div class="overview"><span class="label">Overview:</span> Project Owner presents project and collect Center Staff Feedback</div></div>
    <div class="purpose">7 - <span class="label">Purpose:</span> Provide Center Leaders with Implementation Details<div class="overview" style="padding-left:14px;"><span class="label">Overview:</span> Project Owner presents project and implementation details to ensure Center Leaders are prepared.</div></div>
  </section>

  <section class="phases">
    <div class="phase" style="top:10px;"><div class="phase-icon" role="img" aria-label="Drafting tools icon"><span></span></div><div class="phase-tag">Planning &amp; Design Phase: 1 to 6</div></div>
    <div class="phase" style="top:77px;"><div class="phase-icon" role="img" aria-label="Planning board icon"><span></span></div><div class="phase-tag">Prepare Phase: 7 to 9</div></div>
    <div class="phase" style="top:142px;"><div class="phase-icon" role="img" aria-label="Desk with briefcase icon"><span></span></div><div class="phase-tag">Follow up &amp; Evaluate Phase: 10</div></div>
  </section>

  <section class="channels">
    <div class="ribbon meetings">Meetings</div>
    <div class="channel-steps" style="top:79px;">Steps: 2 - 4 - 5 - 6 - 7</div>
    <div class="ribbon tools">Emails/Tools</div>
    <div class="channel-steps" style="top:147px;">Steps: 8 - 9 - 10</div>
  </section>
</div>
</body>
</html>
```